Boilermaker / Fitter Job Add

We are requiring some nice job add posters for hiring boilermakers or Fitters.
We would like the add to be supplied in a format that we can easily update and change text depending on the situation and details etc,
The job is specific to mining, so pictures in the background that could potentially be used could involve Washplant, draglines, excavators, electric shovel, dozer, actions shots of welding / grinding etc

I have attached some screenshots of adds I have seen recently that stand out.

Our company is KORB ENGINEERING SERVICES PTY LTD.

We would like on the add
CONTACT NUMBER - 0417 358 264
EMAIL admin@ korbengineering.com.au

Some things we could highlight

Full time Position
Own Work Vehicle
Flexible Roster
Local Mackay Company

```html
<!DOCTYPE html>
<html lang="en">
<head>
<meta charset="UTF-8">
<title>Boilermaker / Fitter – Job Ad</title>
<link rel="stylesheet" href="https://fonts.googleapis.com/css2?family=Bebas+Neue&family=Oswald:wght@400;500&display=swap">
<style>
  :root {
    --page: #ffffff;
    --ink-black: #0c0c0c;
    --accent-orange: #f4a43a;
    --text-dark: #1e1e1e;
    --text-light: #ffffff;
    --photo-deep: #1b2a3a;
    --photo-blue: #4a7fa6;
    --photo-spark: #e88a2c;
  }
  html, body {
    margin: 0;
    padding: 0;
    width: 1200px;
    height: 1200px;
    overflow: hidden;
    background: var(--page);
  }
  .job-ad {
    position: absolute;
    left: 91px;
    top: 137px;
    width: 1080px;
    height: 806px;
    background: var(--accent-orange);
    overflow: hidden;
  }
  .job-ad__header {
    position: absolute;
    left: 0;
    top: 0;
    width: 100%;
    height: 149px;
    background: var(--ink-black);
    display: flex;
    align-items: center;
    padding-left: 14px;
    box-sizing: border-box;
  }
  .job-ad__title {
    margin: 0;
    font-family: "Bebas Neue", "Oswald", sans-serif;
    font-weight: 400;
    font-size: 128px;
    line-height: 1;
    letter-spacing: 1px;
    color: var(--text-light);
    white-space: nowrap;
    padding-top: 10px;
  }
  .job-ad__photo {
    position: absolute;
    left: 623px;
    top: 149px;
    width: 457px;
    height: 657px;
    background:
      radial-gradient(ellipse at 35% 75%, var(--photo-spark) 0%, rgba(232,138,44,0.55) 22%, rgba(232,138,44,0) 50%),
      radial-gradient(ellipse at 75% 20%, var(--photo-blue) 0%, rgba(74,127,166,0.4) 40%, rgba(74,127,166,0) 70%),
      linear-gradient(160deg, #2f4c66 0%, var(--photo-deep) 55%, #3a2616 100%);
  }
  .job-ad__perks {
    position: absolute;
    left: 29px;
    top: 252px;
    margin: 0;
    padding: 0;
    list-style: none;
    font-family: "Oswald", sans-serif;
    font-weight: 400;
    font-size: 46px;
    line-height: 84px;
    color: var(--text-dark);
  }
  .job-ad__perk {
    position: relative;
    padding-left: 46px;
    white-space: nowrap;
  }
  .job-ad__perk::before {
    content: "";
    position: absolute;
    left: 4px;
    top: 37px;
    width: 12px;
    height: 12px;
    border-radius: 50%;
    background: var(--text-dark);
  }
  .job-ad__footer {
    position: absolute;
    left: 0;
    bottom: 0;
    width: 623px;
    height: 114px;
    background: var(--ink-black);
    display: flex;
    align-items: center;
    padding-left: 29px;
    box-sizing: border-box;
  }
  .job-ad__cta {
    font-family: "Oswald", sans-serif;
    font-weight: 400;
    font-size: 46px;
    color: var(--text-light);
    letter-spacing: 0.5px;
  }
</style>
</head>
<body>
  <section class="job-ad">
    <header class="job-ad__header">
      <h1 class="job-ad__title">BOILERMAKER / FITTER</h1>
    </header>
    <div class="job-ad__photo" role="img" aria-label="Action shot of a worker welding with bright orange sparks flying against a cool blue background"></div>
    <ul class="job-ad__perks">
      <li class="job-ad__perk">Full time Position</li>
      <li class="job-ad__perk">Own Work Vehicle</li>
      <li class="job-ad__perk">Flexible Roster</li>
      <li class="job-ad__perk">Local Mackay Company</li>
    </ul>
    <footer class="job-ad__footer">
      <span class="job-ad__cta">CONTACT US</span>
    </footer>
  </section>
</body>
</html>
```